Broschüre für Trovimo-Coach
Sehr schnelle und professionelle Umsetzung. Die Designerin hat inhaltlich mitgedacht und die einzelnen Elemente passend und kreativ platziert. Der Kontakt war außerdem sehr nett. Sehr zu empfehlen!
Zielgruppe
Ich bin Deutschlands erster Trovimo-Coach. Ich zeige Unternehmern, Selbstständigen und Vertrieblern wie sie mit persönlichen Videobotschaften mehr Interessen und Abschlüsse generieren.
Aufgabenstellung
Es soll eine Broschüre grafisch gestaltet werden, die als eBook sowie für den Druck verwendet werden kann.
Format DIN A 4.
Bereitgestellt werden folgende Unterlagen:
(1) Texte und Grob-Struktur in der entsprechenden Reihenfolge.
(2) Die Broschüre soll sich an der Struktur des beigefügten eBooks 'Copper Lantern Drift' orientieren.
(3) Fotos, Logo und Grafikelemente sind beigefügt. Zusätzliches Bildmaterial darf eingesetzt werden.
(4) Ein 'Brand Look' mit Farben, Schriftarten und Stil-Elementen ist beigefügt.
(5) Druckvorlage gemäß beigefügter Vorlage von Papyrano. Für den Druck müssen es 20 oder 24 Seiten sein.
Bitte grafisch an meiner Website orientieren: www.haraldkunzo.de

```html
<!DOCTYPE html>
<html lang="de">
<head>
<meta charset="utf-8">
<title>Trovimo-Coach Broschüre – Seiten 06/07</title>
<link rel="stylesheet" href="https://fonts.googleapis.com/css2?family=Poppins:wght@400;500;600;700&family=Permanent+Marker&display=swap">
<style>
  :root {
    --bg: #e4e4e4;
    --paper: #f7f7f6;
    --ink: #1f1d33;
    --violet: #7a36ee;
    --violet-deep: #6f24ea;
    --violet-light: #b387f7;
    --lavender: #dccbff;
    --lime: #e3f65a;
    --lime-soft: rgba(227, 246, 90, .55);
    --diagram-blue: #2f50b0;
    --green: #1f9a3a;
  }
  * { box-sizing: border-box; margin: 0; padding: 0; }
  html, body { width: 1200px; height: 1200px; overflow: hidden; }
  body { background: var(--bg); font-family: "Poppins", sans-serif; color: var(--ink); position: relative; }

  .spread { position: absolute; left: 60px; top: 200px; width: 1080px; height: 800px; display: flex; box-shadow: 0 18px 40px rgba(0,0,0,.18); }
  .page { position: relative; width: 540px; height: 800px; overflow: hidden; }
  .page--left { background: var(--paper); }
  .page--right { background: linear-gradient(90deg, var(--violet-deep) 0%, var(--violet-light) 38%, var(--violet) 70%, var(--violet-deep) 100%); color: #fff; }

  .deco { position: absolute; border-radius: 50%; }
  .deco--left-top { left: 230px; top: -120px; width: 330px; height: 200px; background: radial-gradient(closest-side, var(--lime-soft), transparent); }
  .deco--left-bottom { left: 330px; top: 640px; width: 260px; height: 220px; background: radial-gradient(closest-side, var(--lime-soft), transparent); }
  .deco--right-bottom { left: 300px; top: 620px; width: 300px; height: 240px; background: radial-gradient(closest-side, var(--lime-soft), transparent); }

  .running-head { position: absolute; top: 32px; font-size: 9px; display: flex; align-items: center; gap: 10px; }
  .page--left .running-head { left: 34px; }
  .page--right .running-head { right: 34px; color: var(--ink); }
  .running-head .divider { width: 1px; height: 16px; background: var(--ink); }

  .content { position: absolute; }
  .page--left .content { left: 56px; top: 102px; width: 316px; }

  .section-title { color: var(--violet); font-weight: 600; font-size: 22px; line-height: 1.25; margin-bottom: 18px; }
  .lead, .body-text { font-size: 10.5px; line-height: 14px; margin-bottom: 14px; }
  .lead { font-weight: 500; }
  .label { font-size: 10.5px; font-weight: 500; margin: 6px 0 12px; }

  .icon-row { display: flex; gap: 10px; margin-bottom: 22px; width: 350px; }
  .icon-row svg, .icon-row .video-thumb { width: 34px; height: 34px; flex: none; }
  .video-thumb { border-radius: 3px; background: linear-gradient(180deg, #7aa6d8 0%, #3a5f8c 100%); border: 2px solid #222; }

  .motto { font-family: "Permanent Marker", "Poppins", sans-serif; color: var(--violet); font-size: 14px; font-weight: 700; font-variant: small-caps; margin: 18px 0 16px; letter-spacing: .4px; }

  .flow { position: absolute; left: 56px; top: 640px; width: 290px; height: 114px; }
  .flow-box { position: absolute; top: 0; width: 98px; height: 112px; border: 1.5px solid var(--violet); background: #fff; }
  .flow-box--kunde { left: 186px; border-color: #888; }
  .flow-box__head { background: var(--diagram-blue); color: #fff; font-size: 8px; font-weight: 600; text-align: center; padding: 2px 0; }
  .flow-box__art { margin: 6px; height: 84px; background: linear-gradient(180deg, #ececec, #d6d6d6); }
  .flow-arrow { position: absolute; left: 100px; top: 56px; width: 84px; height: 10px; }
  .flow-note { position: absolute; left: 100px; width: 84px; text-align: center; font-size: 6.5px; font-weight: 700; line-height: 1.2; }
  .flow-note--top { top: 20px; }
  .flow-note--bottom { top: 68px; color: var(--green); }

  .page--right .content { left: 62px; top: 80px; width: 440px; }
  .spread-title { color: var(--lavender); font-weight: 600; font-size: 19px; line-height: 23px; margin-bottom: 26px; }
  .page--right .body-text { margin-left: 6px; width: 330px; }
  .mistakes-title { color: var(--lavender); font-weight: 600; font-size: 12.5px; line-height: 16px; margin: 22px 0 14px 64px; width: 270px; }
  .mistakes { list-style: none; margin-left: 10px; }
  .mistakes li { display: flex; align-items: center; gap: 26px; margin-bottom: 13px; }
  .mistakes .num { width: 28px; height: 28px; border-radius: 50%; background: var(--lime); color: var(--ink); font-size: 9px; font-weight: 700; display: grid; place-items: center; flex: none; }
  .mistakes .text { color: var(--lime); font-size: 10.5px; font-weight: 500; line-height: 14px; width: 320px; }

  .solutions { display: grid; grid-template-columns: 196px 200px; column-gap: 18px; margin: 28px 0 0 6px; }
  .solution { margin-bottom: 16px; }
  .solution h3 { font-size: 10.5px; font-weight: 600; line-height: 14px; color: var(--ink); margin-bottom: 6px; }
  .solution p { font-size: 10.5px; line-height: 14px; color: #fff; }
</style>
</head>
<body>
  <div class="spread">
    <section class="page page--left">
      <div class="deco deco--left-top" role="img" aria-label="Dekoratives Wellenelement in Limettengrün"></div>
      <div class="deco deco--left-bottom" role="img" aria-label="Dekoratives Wellenelement in Limettengrün"></div>
      <div class="running-head"><span>06</span><span class="divider"></span><span>www.haraldkunzo.de</span></div>

      <div class="content">
        <h2 class="section-title">2. Video Selling<br>Eine kurze Einführung</h2>
        <p class="lead">VideoSelling bedeutet, dass Du an spezifischen Punkten in Deinem Vertriebsprozess gesichtslose und langweile Text­nachrichten durch persönliche Videobotschaften ersetzt.</p>
        <p class="body-text">Denn: Die stärkste Kraft im Vertrieb bist Du selbst. Du machst den Unterschied.</p>
        <p class="body-text">Grafisch vereinfacht sieht das in etwa wie folgt aus:</p>

        <svg width="0" height="0" style="position:absolute">
          <symbol id="mail" viewBox="0 0 34 34">
            <rect x="9" y="2" width="16" height="16" fill="#fff" stroke="#222" stroke-width="2"/>
            <text x="17" y="14" font-size="10" font-family="Poppins, sans-serif" text-anchor="middle" fill="#222">@</text>
            <path d="M3 14 L17 24 L31 14 V31 H3 Z" fill="#fff" stroke="#222" stroke-width="2.4" stroke-linejoin="round"/>
            <path d="M3 31 L14 21 M31 31 L20 21" stroke="#222" stroke-width="2.4"/>
          </symbol>
        </svg>

        <p class="label">Vorher:</p>
        <div class="icon-row">
          <svg><use href="#mail"/></svg><svg><use href="#mail"/></svg><svg><use href="#mail"/></svg><svg><use href="#mail"/></svg>
          <svg><use href="#mail"/></svg><svg><use href="#mail"/></svg><svg><use href="#mail"/></svg><svg><use href="#mail"/></svg>
        </div>
        <p class="label">Nachher:</p>
        <div class="icon-row">
          <div class="video-thumb" role="img" aria-label="Videobotschaft: Foto des Coaches auf einem Bildschirm"></div>
          <svg><use href="#mail"/></svg>
          <div class="video-thumb" role="img" aria-label="Videobotschaft: Foto des Coaches auf einem Bildschirm"></div>
          <svg><use href="#mail"/></svg><svg><use href="#mail"/></svg><svg><use href="#mail"/></svg>
          <div class="video-thumb" role="img" aria-label="Videobotschaft: Foto des Coaches auf einem Bildschirm"></div>
          <svg><use href="#mail"/></svg>
        </div>

        <p class="body-text">Bleibe im gesamten Vertriebsprozess als Verkäufer sicht­bar. Oder wie es in den USA heißt:</p>
        <p class="motto">„Keep your face in the race!“</p>
        <p class="body-text">Eine persönliche Videobotschaft ist ein 1:1-Video, das Du für einen bestimmten Kunden oder ein kleines Team auf­nimmst. Eine hohe Personalisierung ist der Schlüssel, mit dem Du viele neue Türen bei Deinen Kunden öffnest.</p>
      </div>

      <div class="flow">
        <div class="flow-box">
          <div class="flow-box__head">Vertrieb</div>
          <div class="flow-box__art" role="img" aria-label="Illustration: Verkäufer nimmt am Schreibtisch und per Smartphone ein Video auf"></div>
        </div>
        <p class="flow-note flow-note--top">Persönliches<br>1:1-Video</p>
        <svg class="flow-arrow" viewBox="0 0 84 10" aria-hidden="true"><path d="M0 5 H80 M74 1 L82 5 L74 9" fill="none" stroke="#222" stroke-width="1.4"/></svg>
        <p class="flow-note flow-note--bottom">Ortunabhängig<br>Zeitunabhängig</p>
        <div class="flow-box flow-box--kunde">
          <div class="flow-box__head">Kunde</div>
          <div class="flow-box__art" role="img" aria-label="Illustration: Kunde empfängt das Video auf dem Smartphone"></div>
        </div>
      </div>
    </section>

    <section class="page page--right">
      <div class="deco deco--right-bottom" role="img" aria-label="Dekoratives Wellenelement in Limettengrün"></div>
      <div class="running-head"><span>www.haraldkunzo.de</span><span class="divider"></span><span>07</span></div>

      <div class="content">
        <h2 class="spread-title">Darum lässt Du Umsatz auf der<br>Straße liegen:</h2>
        <p class="body-text">Während Online-Marketer den Einsatz von Videos bereits perfekt verstehen und wissen, dass Bewegtbilder in der Werbung besser funktionieren als Text oder Grafiken, haben die meisten Vertriebler dieses Konzept in ihrer Kun­denkommunikation nicht einmal ansatzweise verstanden.</p>

        <h3 class="mistakes-title">Die drei größten Fehler, die Verkäufer online machen, sind:</h3>
        <ol class="mistakes">
          <li><span class="num">1.</span><span class="text">Sie warten auf die nächste Videokonferenz, um sich zu zeigen.</span></li>
          <li><span class="num">2.</span><span class="text">Sie kommunizieren auf Social Media ausschließlich über Textnachrichten.</span></li>
          <li><span class="num">3.</span><span class="text">Sie denken, dass persönliche Videos zu viel Zeit kosten und nichts bringen.</span></li>
        </ol>

        <div class="solutions">
          <div>
            <div class="solution">
              <h3>Lösung 1:<br>Durchgängige digital Sichtbarkeit</h3>
              <p>Um durchgängig „vor Ort“ zu sein, versendest Du zwischendurch immer wieder ein persönliches Video, um bei Deinen Kunden auch dann präsent zu sein, wenn Du nicht gemeinsam mit ihnen am Tisch sitzt oder Ihr Euch in einer Videokonferenz seht.</p>
            </div>
            <div class="solution">
              <h3>Lösung 2:<br>Persönliche Videos bei der Kon­taktanbahnung</h3>
              <p>Um Sympathie und Vertrauen auf­zubauen, müssen wir uns dem anderen zeigen. Versende daher zu einem frühen Zeitpunkt in der Kon­taktaufnahme auf Netzwerkio &amp; Co. persönliche Videobotschaften. Du schaffst damit die Grundlage für einen vertrauensvollen Austausch zwischen ehrbaren Kaufleuten.</p>
            </div>
          </div>
          <div class="solution">
            <h3>Lösung 3:<br>Videoplattformen mit WOW-Effekt</h3>
            <p>Über speziell für Vertriebler entwi­ckelte Videoplattformen kannst Du mit wenigen Klicks über Deine Webcam oder Dein Smartphone kinderleicht Videos aufnehmen und versenden. Mit persönlichen Videobotschaften hebst Du Dich im überfüllten Posteingang garantiert von allen anderen ab mit garan­tiertem WOW-Effekt.</p>
          </div>
        </div>
      </div>
    </section>
  </div>
</body>
</html>
```